I need a feather flag designed for my business which states " HELICOPTER RIDES" and possibly adding my logo to them. This will be used for my helicopter ride business and we can put these up to show people where the rides will be .

Industry/Entity Type

aviation

Colors
00AB8E
00BBA5
67D7C9
C6EFE9
E9F9F6
EB3D1F
EC4F4E
F09395
F8D3D4
FCEDEE

Requirements
Must have
• logo

```html
<!DOCTYPE html>
<html lang="en">
<head>
<meta charset="utf-8">
<title>Skyward Helicopters – Feather Flag</title>
<link href="https://fonts.googleapis.com/css2?family=Baloo+2:wght@800&family=Montserrat:wght@800&display=swap" rel="stylesheet">
<style>
  :root {
    --teal-deep: #00AB8E;
    --teal: #21a88a;
    --teal-light: #67D7C9;
    --mint: #E9F9F6;
    --red: #EB3D1F;
    --red-soft: #EC4F4E;
    --flag-white: #f7f7f7;
    --ink: #1e2626;
    --backdrop: #e4e4e2;
  }
  * { margin: 0; padding: 0; box-sizing: border-box; }
  html, body {
    width: 1200px;
    height: 920px;
    overflow: hidden;
  }
  body {
    background: radial-gradient(ellipse at 50% 40%, #f1f1ef 0%, var(--backdrop) 70%);
    position: relative;
  }
  .feather-flag {
    position: absolute;
    left: 440px;
    top: 30px;
    width: 320px;
    height: 860px;
  }
  .feather-flag svg {
    position: absolute;
    inset: 0;
    filter: drop-shadow(0 6px 14px rgba(0,0,0,0.12));
  }
  .flag-headline {
    position: absolute;
    left: calc(232px - 330px);
    top: calc(470px - 70px);
    width: 660px;
    height: 140px;
    transform: rotate(-90deg);
    display: flex;
    align-items: center;
    justify-content: center;
    font-family: "Baloo 2", "Arial Rounded MT Bold", sans-serif;
    font-weight: 800;
    font-size: 76px;
    line-height: 1;
    color: #ffffff;
    -webkit-text-stroke: 10px var(--red);
    paint-order: stroke fill;
    white-space: nowrap;
    letter-spacing: 0.5px;
  }
  .brand-mark {
    position: absolute;
    left: calc(72px - 190px);
    top: calc(330px - 50px);
    width: 380px;
    height: 100px;
    transform: rotate(-90deg);
    display: flex;
    align-items: center;
    justify-content: center;
    gap: 14px;
  }
  .brand-dot {
    width: 26px;
    height: 26px;
    border-radius: 50%;
    background: var(--teal-deep);
    flex: none;
  }
  .brand-name {
    font-family: "Montserrat", Arial, sans-serif;
    font-weight: 800;
    color: var(--ink);
    line-height: 1;
    display: flex;
    flex-direction: column;
    align-items: flex-start;
  }
  .brand-name .brand-primary {
    font-size: 44px;
    letter-spacing: 1px;
  }
  .brand-name .brand-secondary {
    font-size: 15px;
    letter-spacing: 9px;
    margin-top: 4px;
  }
</style>
</head>
<body>
  <div class="feather-flag">
    <svg width="320" height="860" viewBox="0 0 320 860" aria-hidden="true">
      <defs>
        <clipPath id="feather-shape">
          <path d="M0,860 L0,210 C0,80 110,8 320,0 L320,730 C320,810 262,860 180,860 Z"/>
        </clipPath>
      </defs>
      <g clip-path="url(#feather-shape)">
        <rect class="flag-field-white" x="0" y="0" width="146" height="860" fill="#f7f7f7"/>
        <rect class="flag-field-teal" x="146" y="0" width="174" height="860" fill="#21a88a"/>
      </g>
    </svg>

    <div class="brand-mark">
      <span class="brand-dot"></span>
      <div class="brand-name">
        <span class="brand-primary">SKYWARD</span>
        <span class="brand-secondary">HELICOPTERS</span>
      </div>
    </div>

    <div class="flag-headline">Helicopter Rides</div>
  </div>
</body>
</html>
```